Sumvane financial services stationery design

We need business stationery designed with letterheads, business cards, with compliments and envelope for a business that offers tax and accounting services

Designs look the same

Target Market(s)

Small to medium businesses, individuals, Self managed superfunds

Industry/Entity Type

Business

Font styles to use
Serif
Other font styles liked:
• Atlanta

Colors
32a6d6
3277b5

Requirements
Must have
• Logo incorporated with all my stationery
• professional
Should not have
• Lots of colours
• Busy

```html
<!DOCTYPE html>
<html lang="en">
<head>
<meta charset="utf-8">
<title>Sumvane Financial Services – Stationery</title>
<link rel="stylesheet" href="https://fonts.googleapis.com/css2?family=Cinzel:wght@500&family=Work+Sans:wght@400;500;600&display=swap">
<style>
:root{
  --bg:#ebebeb;
  --paper:#ffffff;
  --blue:#3277b5;
  --sky:#32a6d6;
  --env-blue:#1777c0;
  --ink:#4a4a4a;
  --muted:#9a9a9a;
  --slate:#5b5a5d;
}
*{margin:0;padding:0;box-sizing:border-box}
html,body{width:1200px;height:807px;overflow:hidden;background:var(--bg)}
body{position:relative;font-family:"Work Sans",sans-serif;color:var(--ink)}
.sheet{position:absolute;background:var(--paper);box-shadow:2px 3px 8px rgba(0,0,0,.22)}
.piece{position:absolute}
.logo{position:absolute;display:flex;align-items:center}
.logo-mark{background:linear-gradient(135deg,var(--sky),var(--blue));flex:none}
.logo-text{display:flex;flex-direction:column;line-height:1}
.logo-name{font-family:"Cinzel",serif;font-weight:500;color:var(--ink);letter-spacing:.5px}
.logo-sub{font-family:"Cinzel",serif;font-weight:500;color:var(--ink);letter-spacing:1.6px;text-transform:uppercase}
.logo.on-dark .logo-mark{background:#fff}
.logo.on-dark .logo-name,.logo.on-dark .logo-sub{color:#fff}
.divider{position:absolute;width:1.5px;background:var(--blue)}
.contact{position:absolute;color:var(--ink);line-height:1.35}
.contact .row{display:flex;align-items:center;gap:4px}
.contact svg{flex:none}
.contact .web b{color:var(--blue);font-weight:inherit}
.contact .gap{height:4px}
.letter .greeting{position:absolute;left:34px;top:211px;font-size:15px;color:#7a7a7a}
.letter .body{position:absolute;left:34px;top:248px;width:440px;font-size:9.4px;line-height:13.3px;color:var(--muted)}
.letter .body p{margin-bottom:18px}
.signature{position:absolute;left:34px;top:556px;width:124px;height:26px;background:linear-gradient(90deg,#ececec,#f6f6f6);border-radius:3px}
.card-name{font-size:8.5px;font-weight:600;color:var(--blue);letter-spacing:.2px}
.card-role{font-size:6px;color:var(--ink);margin-bottom:4px}
.flap{position:absolute;left:0;top:0}
</style>
</head>
<body>

<!-- Letterhead -->
<section class="sheet piece letter" style="left:54px;top:42px;width:508px;height:720px">
  <div class="logo" style="left:32px;top:48px">
    <span class="logo-mark" style="width:50px;height:50px"></span>
    <span class="logo-text" style="margin-left:10px">
      <span class="logo-name" style="font-size:30px">Sumvane</span>
      <span class="logo-sub" style="font-size:7.8px;margin-top:2px;margin-left:5px">Financial Services</span>
    </span>
  </div>
  <div class="divider" style="left:293px;top:44px;height:58px"></div>
  <div class="contact" style="left:360px;top:41px;font-size:10px">
    <div>48 Harbour Lane,</div>
    <div>Montreal, Qc H2X 3K7</div>
    <div class="gap"></div>
    <div class="row"><svg width="6" height="7" viewBox="0 0 6 7"><path d="M1 0h1.5l.5 2-1 .6a4 4 0 0 0 1.6 1.8l.6-1 2 .5V5.4C6 6.3 5 7 4 6.6 2 6 .6 4.4 0 2.4-.3 1.2.3 0 1 0z" fill="var(--blue)"/></svg>514.555.0142</div>
    <div class="row"><svg width="7" height="5" viewBox="0 0 7 5"><rect x=".4" y=".4" width="6.2" height="4.2" fill="none" stroke="var(--blue)" stroke-width=".8"/><path d="M.4.4 3.5 3 6.6.4" fill="none" stroke="var(--blue)" stroke-width=".8"/></svg>info@Sumvanefs.com</div>
    <div class="row web"><svg width="7" height="7" viewBox="0 0 7 7"><circle cx="3.5" cy="3.5" r="3.5" fill="var(--blue)"/></svg>www.<b>Sumvanefs</b>.com</div>
  </div>
  <div class="greeting">Dear sir,</div>
  <div class="body">
    <p>Lorem ipsum dolor sit amet, an vel recteque dissentiet, detracto albucius platonem ex vel, eros repudiandae cu. Atqui aliquando nec an, unum graece adolescens vel ad. Id odio scae has, iudico euismod atomorum ius ea, cum ea honestatis quaerendum theophrastus. Mea honestatis quaerendum theophrastus. Mea</p>
    <p>Lorem ipsum dolor sit amet, an vel recteque dissentiet, detracto albucius platonem ex vel, eros repudiandae cu. Atqui aliquando nec an, unum graece adolescens vel ad. Id odio scae has, iudico euismod atomorum ius ea, cum ea honestatis quaerendum theophrastus. Mea doming repudiandae ex, cu cum civibus assentior posidonium. Quo etiam pertinax ex, te eros repudiandae cu. Atqui aliquando nec an, unum graece adolescens vel ad. Id odio scae honestatis quaerendum theophrastus. Mea</p>
    <p>Lorem ipsum dolor sit amet, an vel recteque dissentiet, detracto albucius platonem ex vel, eros repudiandae cu. Atqui aliquando nec an, unum graece adolescens vel ad. Id odio scae has, iudico euismod atomorum ius ea, cum ea honestatis quaerendum theophrastus. Mea honestatis quaerendum theophrastus. Mea</p>
    <p>eros repudiandae cu. Atqui aliquando nec an, unum graece adolescens vel ad. Id odio scae honestatis quaerendum theophrastus. Mea posidonium. Quo etiam pertinax ex, te<br>etiam pertinax ex, te</p>
  </div>
  <div class="signature" role="img" aria-label="Handwritten signature of Daniel Marsh"></div>
</section>

<!-- Business card front -->
<section class="sheet piece" style="left:631px;top:43px;width:245px;height:139px">
  <div class="logo" style="left:23px;top:57px">
    <span class="logo-mark" style="width:27px;height:27px"></span>
    <span class="logo-text" style="margin-left:6px">
      <span class="logo-name" style="font-size:16px">Sumvane</span>
      <span class="logo-sub" style="font-size:4.2px;margin-top:1px;margin-left:3px">Financial Services</span>
    </span>
  </div>
  <div class="divider" style="left:138px;top:40px;height:60px;width:1px"></div>
  <div class="contact" style="left:150px;top:38px;font-size:5.8px;line-height:1.4">
    <div class="card-name">DANIEL MARSH</div>
    <div class="card-role">Owners</div>
    <div>48 Harbour Lane,</div>
    <div>Montreal, Qc H2X 3K7</div>
    <div class="row"><svg width="4" height="5" viewBox="0 0 6 7"><path d="M1 0h1.5l.5 2-1 .6a4 4 0 0 0 1.6 1.8l.6-1 2 .5V5.4C6 6.3 5 7 4 6.6 2 6 .6 4.4 0 2.4-.3 1.2.3 0 1 0z" fill="var(--blue)"/></svg>514.555.0142</div>
    <div class="row"><svg width="5" height="4" viewBox="0 0 7 5"><rect x=".4" y=".4" width="6.2" height="4.2" fill="none" stroke="var(--blue)" stroke-width=".8"/></svg>info@Sumvanefs.com</div>
    <div class="row web"><svg width="4" height="4" viewBox="0 0 7 7"><circle cx="3.5" cy="3.5" r="3.5" fill="var(--blue)"/></svg>www.<b>Sumvanefs</b>.com</div>
  </div>
</section>

<!-- Business card back -->
<section class="sheet piece" style="left:889px;top:43px;width:246px;height:140px;background:var(--slate)">
  <div class="logo on-dark" style="left:58px;top:54px">
    <span class="logo-mark" style="width:34px;height:34px"></span>
    <span class="logo-text" style="margin-left:8px">
      <span class="logo-name" style="font-size:20px">Sumvane</span>
      <span class="logo-sub" style="font-size:5px;margin-top:1px;margin-left:3px">Financial Services</span>
    </span>
  </div>
</section>

<!-- Envelope back with flap -->
<section class="sheet piece" style="left:631px;top:222px;width:503px;height:252px">
  <svg class="flap" width="503" height="77" viewBox="0 0 503 77">
    <path d="M0 0H503L496 40Q492 76 456 76H47Q11 76 7 40Z" fill="var(--env-blue)"/>
  </svg>
  <div class="logo on-dark" style="left:193px;top:24px">
    <span class="logo-mark" style="width:30px;height:30px"></span>
    <span class="logo-text" style="margin-left:7px">
      <span class="logo-name" style="font-size:18px">Sumvane</span>
      <span class="logo-sub" style="font-size:4.6px;margin-top:1px;margin-left:3px">Financial Services</span>
    </span>
  </div>
</section>

<!-- Envelope front -->
<section class="sheet piece" style="left:631px;top:512px;width:503px;height:250px">
  <div class="logo" style="left:22px;top:179px">
    <span class="logo-mark" style="width:44px;height:44px"></span>
    <span class="logo-text" style="margin-left:9px">
      <span class="logo-name" style="font-size:26px">Sumvane</span>
      <span class="logo-sub" style="font-size:6.8px;margin-top:2px;margin-left:4px">Financial Services</span>
    </span>
  </div>
  <div class="divider" style="left:212px;top:172px;height:56px"></div>
  <div class="contact" style="left:238px;top:169px;font-size:9px">
    <div>48 Harbour Lane,</div>
    <div>Montreal, Qc H2X 3K7</div>
    <div class="gap"></div>
    <div class="row"><svg width="5" height="6" viewBox="0 0 6 7"><path d="M1 0h1.5l.5 2-1 .6a4 4 0 0 0 1.6 1.8l.6-1 2 .5V5.4C6 6.3 5 7 4 6.6 2 6 .6 4.4 0 2.4-.3 1.2.3 0 1 0z" fill="var(--blue)"/></svg>514.555.0142</div>
    <div class="row"><svg width="6" height="5" viewBox="0 0 7 5"><rect x=".4" y=".4" width="6.2" height="4.2" fill="none" stroke="var(--blue)" stroke-width=".8"/><path d="M.4.4 3.5 3 6.6.4" fill="none" stroke="var(--blue)" stroke-width=".8"/></svg>info@Sumvanefs.com</div>
    <div class="row web"><svg width="6" height="6" viewBox="0 0 7 7"><circle cx="3.5" cy="3.5" r="3.5" fill="var(--blue)"/></svg>www.<b>Sumvanefs</b>.com</div>
  </div>
</section>

</body>
</html>
```